New Website for IT Services Business

We need an uncoded web design for a new company based in Australia called "Falcon IT". We offer specialised point of sale (POS) support to the hospitality industry. We already support hundreds of cafes and restaurants. We are also about to launch and promote a range of new services with the offering of General IT Support being the most important. Other additional services to be offered are Falcon Vault Storage, reselling and supporting Corvel Shieldware and Trelmo Suite.

We have a logo design and our colour scheme is based on the logo with the addition of charcoal grey (see attached logos). We want the pages to reflect precision and efficiency with sharp characteristics. It must be professional but playful/fun elements are encouraged.

Our target audience is restaurant and cafe owners who are interested in finding high quality POS and IT support for their business.

The main call to action on the home page should be either 'Let's Meet For Coffee!' or 'Find out more (by completing a form)'. If you are unsure about what the general text should say then you can use 'Lorem Ipsum' where required.

The site must be viewable at different resolutions and on smart phones and tablets.

The website structure will be quite simple. We require:
- one impressive landing page. Visitors will quickly determine our services and that we provide a very high level of service while also offering value for money. Obviously a clear list of links (however/wherever you like) to the other pages.
- Simple pages with a similar layout for the following:
- Services - "POS & IT Support for the Hospitality Industry" being the main one. With complementary services also listed. Another call to action on this page with the option of 'Let's Meet For Coffee' or a "More information/Pricing" form to be completed by the visitor.
- Products - will be a small online storefront for a few simple products.
- About - Business background. 2x Directors with a photo and brief Bio.
- Downloads - A list of free files to download. Includes remote access client software.
- Contact Us - Mailing address, Email addresses and Support phone number.

Please feel free to ask any questions about the design. I will assist as much as possible.

Thank you for viewing. We promise to give constructive feedback to every person who submits a design. Thank you so much.

Target Market(s)

Restaurant and Cafe owners.

Industry/Entity Type

Hospitality

Requirements
Must have
• - Viewable on different resolutions and on smart phones and tablets.
- Clear call to action of EITHER 'Let's Meet For Coffee' or a "More information/Pricing" form to be completed by the visitor.

```html
<!DOCTYPE html>
<html lang="en">
<head>
<meta charset="utf-8">
<title>Falcon IT – POS &amp; IT Support for Hospitality</title>
<link rel="stylesheet" href="https://fonts.googleapis.com/css2?family=Oswald:wght@400;600;700&family=Open+Sans:ital,wght@0,400;0,600;0,700;1,400&family=Noto+Serif&family=Caveat&family=Poiret+One&display=swap">
<style>
:root{
  --red:#d52b3b;
  --red-dark:#a81c2a;
  --charcoal:#3b3b3e;
  --charcoal-dark:#252527;
  --ink:#404040;
  --muted:#6b6b6b;
  --page:#e7e7e7;
  --white:#ffffff;
  --sky:#1fb1e6;
  --sky-dark:#0f8fc6;
  --footer:#222223;
}
*{box-sizing:border-box;margin:0;padding:0}
html,body{width:790px;height:1200px;overflow:hidden;background:var(--page)}
.page{position:absolute;left:0;top:0;width:700px;height:1063px;transform:scale(1.12857);transform-origin:0 0;
  font-family:"Open Sans",sans-serif;color:var(--ink);
  background:repeating-linear-gradient(90deg,#e9e9e9 0 3px,#e3e3e3 3px 4px)}
.abs{position:absolute}

/* header */
.topbar{left:0;top:0;width:700px;height:42px;background:linear-gradient(#e23646,var(--red-dark))}
.brand{left:68px;top:0;width:127px;height:68px;background:var(--white);clip-path:polygon(0 0,100% 0,100% 86%,0 100%);
  box-shadow:0 2px 4px rgba(0,0,0,.3);display:flex;align-items:center;gap:6px;padding:0 0 10px 12px}
.brand-dot{width:18px;height:18px;border-radius:50%;background:var(--red)}
.brand-name{font-family:"Oswald",sans-serif;font-weight:700;font-size:20px;color:var(--charcoal)}
.nav{left:250px;top:0;height:42px;display:flex;align-items:center;font-family:"Oswald",sans-serif;font-weight:600;font-size:12px}
.nav a{color:var(--white);text-decoration:none;padding:0 9px;border-right:1px solid rgba(255,255,255,.25);line-height:14px}
.nav a:last-child{border-right:0}
.nav a.current{background:var(--charcoal-dark);padding:4px 11px;transform:skewX(-12deg);border:0;margin-right:1px}
.social{left:585px;top:13px;display:flex;gap:2px}
.social span{width:14px;height:14px;border-radius:50%;background:#2f77c4;border:1px solid #fff}

/* hero */
.hero{left:0;top:42px;width:700px;height:274px;background:linear-gradient(100deg,#545a60 0%,#8b8f92 30%,#c9c4bd 55%,#7b7671 80%,#3e3f43 100%)}
.hero-edge{left:0;top:309px;width:700px;height:8px}
.hero-band{left:92px;top:158px;width:510px;height:48px;background:rgba(40,40,40,.55);clip-path:polygon(4% 0,100% 0,100% 100%,0 100%)}
.hero-title{left:118px;top:158px;font-family:"Oswald",sans-serif;font-weight:700;font-size:25px;color:var(--white);letter-spacing:-.3px;text-shadow:0 1px 2px rgba(0,0,0,.5)}
.hero-sub{left:481px;top:187px;font-family:"Oswald",sans-serif;font-weight:600;font-size:11px;color:var(--red)}
.hero-copy{left:116px;top:214px;width:470px;font-size:9.6px;line-height:13px;color:#f3f3f3}
.thumbs{left:116px;top:262px;display:flex;gap:2px}
.thumbs span{width:32px;height:16px;background:linear-gradient(#9ea3a8,#60656a)}
.cta-coffee{left:460px;top:256px;width:137px;height:36px;background:linear-gradient(var(--sky),var(--sky-dark));
  clip-path:polygon(6% 0,100% 0,100% 100%,0 100%);color:var(--white);font-family:"Oswald",sans-serif;font-weight:600;font-size:10.5px;
  display:flex;align-items:center;justify-content:center;padding-left:6px}
.arrow{top:145px}

/* section tabs */
.tab{height:35px;background:var(--white);display:flex;align-items:center;justify-content:center;
  font-family:"Oswald",sans-serif;font-weight:600;font-size:15px;color:var(--charcoal)}
.tab-featured{left:235px;top:318px;width:232px;clip-path:polygon(0 0,100% 0,96% 100%,55% 100%,50% 112%,45% 100%,4% 100%)}
.tab-additional{left:217px;top:775px;width:240px;height:34px;clip-path:polygon(5% 0,95% 0,100% 100%,0 100%);font-family:"Open Sans",sans-serif;font-size:14px}

/* feature circles */
.feature{width:150px;text-align:center}
.ring{width:148px;height:148px;border-radius:50%;border:1px solid #d6d6d6;background:#ececec;display:flex;align-items:center;justify-content:center;margin:0 auto}
.disc{width:120px;height:120px;border-radius:50%;color:var(--white);display:flex;flex-direction:column;align-items:center;justify-content:center;
  font-family:"Oswald",sans-serif;font-weight:600;font-size:13.5px;line-height:14px;box-shadow:0 3px 5px rgba(0,0,0,.3)}
.disc-dark{background:radial-gradient(circle at 50% 30%,#5a5a5e,var(--charcoal-dark))}
.disc-red{background:radial-gradient(circle at 50% 30%,#ec3e4e,var(--red-dark))}
.disc svg{margin-bottom:6px}
.feature p{font-size:7.6px;line-height:9.6px;color:var(--muted);margin:8px auto 0;width:136px}
.btn-more{display:inline-block;width:55px;height:12px;background:linear-gradient(var(--sky),var(--sky-dark));color:var(--white);
  font-size:6.5px;line-height:12px;text-align:center;clip-path:polygon(5% 0,100% 0,95% 100%,0 100%)}
.feature .btn-more{margin-top:5px}

/* general support panel */
.panel{left:68px;top:596px;width:562px;height:152px;background:var(--white);box-shadow:0 0 3px rgba(0,0,0,.15)}
.panel h2{position:absolute;left:24px;top:22px;font-family:"Oswald",sans-serif;font-weight:700;font-size:27px;line-height:29px;color:var(--charcoal);letter-spacing:-.3px}
.panel p{position:absolute;left:24px;top:88px;width:270px;font-size:8.3px;line-height:12px;color:var(--ink)}
.panel-photo{left:315px;top:25px;width:227px;height:104px;background:linear-gradient(110deg,#d7d2c7,#a7a39a 45%,#7d8086);clip-path:polygon(0 0,97% 0,100% 100%,0 98%)}
.cta-red{left:307px;top:110px;width:97px;height:24px;background:linear-gradient(#de3343,var(--red-dark));color:var(--white);
  font-family:"Oswald",sans-serif;font-weight:600;font-size:8px;display:flex;align-items:center;justify-content:center;transform:rotate(-2deg)}

/* additional services */
.rule{left:68px;top:808px;width:562px;height:1px;background:#d2d2d2}
.svc{left:68px;height:23px;color:var(--white);font-family:"Open Sans",sans-serif;font-weight:700;font-size:10px;display:flex;align-items:center;gap:6px;padding-left:8px;
  background:linear-gradient(#4a4a4d,var(--charcoal-dark));box-shadow:0 2px 3px rgba(0,0,0,.3)}
.svc-active{height:37px;background:linear-gradient(#e13646,var(--red-dark));clip-path:polygon(0 0,90% 0,100% 50%,90% 100%,0 100%);line-height:11px}
.svc-copy{left:283px;top:828px;width:350px;font-family:"Noto Serif",serif;font-size:8.3px;line-height:12.4px;color:var(--ink)}

/* footer */
.footer{left:0;top:953px;width:700px;height:60px;background:var(--footer)}
.footer-links{top:970px;font-size:7.2px;line-height:8.6px;color:var(--white)}
.call-label{left:220px;top:961px;font-family:"Caveat",cursive;font-size:10px;color:var(--white)}
.phone{left:207px;top:972px;font-family:"Poiret One",sans-serif;font-size:21px;color:var(--red);letter-spacing:.5px}
.footer-note{left:416px;top:975px;font-size:8px;line-height:10px;font-style:italic;color:var(--white)}
.footer-note a{color:var(--sky);text-decoration:underline}
.legal{left:0;top:1022px;width:700px;text-align:center;font-size:7.5px;color:var(--muted)}
</style>
</head>
<body>
<div class="page">

  <header>
    <div class="abs topbar"></div>
    <div class="abs brand"><span class="brand-dot"></span><span class="brand-name">Falcon IT</span></div>
    <nav class="abs nav">
      <a href="#">Home</a><a href="#" class="current">About</a><a href="#">Services</a><a href="#">Products</a><a href="#">Downloads</a><a href="#">Contact</a>
    </nav>
    <div class="abs social" aria-label="Social links"><span></span><span></span><span></span></div>
  </header>

  <section class="hero-section">
    <div class="abs hero" role="img" aria-label="Photo of three smiling businessmen in suits talking over coffee"></div>
    <svg class="abs hero-edge" width="700" height="8" viewBox="0 0 700 8" aria-hidden="true">
      <pattern id="zig" width="6" height="8" patternUnits="userSpaceOnUse"><path d="M0 8 L3 2 L6 8 Z" fill="#e7e7e7"/></pattern>
      <rect width="700" height="8" fill="url(#zig)"/>
    </svg>
    <svg class="abs arrow" style="left:36px" width="22" height="36" viewBox="0 0 22 36" aria-hidden="true"><path d="M18 2 L4 18 L18 34" fill="none" stroke="rgba(255,255,255,.7)" stroke-width="2"/></svg>
    <svg class="abs arrow" style="left:642px" width="22" height="36" viewBox="0 0 22 36" aria-hidden="true"><path d="M4 2 L18 18 L4 34" fill="none" stroke="rgba(255,255,255,.7)" stroke-width="2"/></svg>
    <div class="abs hero-band"></div>
    <h1 class="abs hero-title">We Offer Specialized Point of Sale Support to the</h1>
    <div class="abs hero-sub">Hospitality Industry</div>
    <p class="abs hero-copy">We Support Hundreds of Cafes and Restaurants. Lorem Ipsum is simply dummy text of the printing and typesetting industry. Lorem Ipsum has been the industry standard dummy text ever since when an unknown printer took a galley of type and scrambled it to make a type specimen book.</p>
    <div class="abs thumbs" role="img" aria-label="Slide thumbnails"><span></span><span></span><span></span><span></span></div>
    <a class="abs cta-coffee">LET'S MEET &nbsp;FOR COFFEE</a>
  </section>

  <section class="featured">
    <h2 class="abs tab tab-featured">Falcon's Featured Services</h2>

    <div class="abs feature" style="left:113px;top:367px">
      <div class="ring"><div class="disc disc-dark">
        <svg width="18" height="26" viewBox="0 0 18 26" aria-hidden="true"><rect x="2" y="1" width="14" height="24" rx="2" fill="#fff"/><rect x="5" y="4" width="8" height="5" fill="#3b3b3e"/><g fill="#3b3b3e"><rect x="5" y="11" width="2" height="2"/><rect x="8" y="11" width="2" height="2"/><rect x="11" y="11" width="2" height="2"/><rect x="5" y="15" width="2" height="2"/><rect x="8" y="15" width="2" height="2"/><rect x="11" y="15" width="2" height="2"/><rect x="5" y="19" width="2" height="2"/><rect x="8" y="19" width="2" height="2"/><rect x="11" y="19" width="2" height="2"/></g></svg>
        <span>POS &amp;<br>IT Support</span></div></div>
      <p>Lorem Ipsum is simply dummy text the printing galley of type and scrambled it to make a type</p>
      <a class="btn-more">Learn More</a>
    </div>

    <div class="abs feature" style="left:277px;top:367px">
      <div class="ring"><div class="disc disc-red">
        <svg width="28" height="26" viewBox="0 0 28 26" aria-hidden="true"><path d="M2 2 H26 V18 H12 L6 24 V18 H2 Z" fill="#fff"/><text x="14" y="15" text-anchor="middle" font-family="Oswald,sans-serif" font-weight="700" font-size="13" fill="#d52b3b">$</text></svg>
        <span>Offering Value<br>for Money</span></div></div>
      <p>Lorem Ipsum is simply dummy text the printing galley of type and scrambled it to make a type</p>
      <a class="btn-more">Learn More</a>
    </div>

    <div class="abs feature" style="left:436px;top:367px">
      <div class="ring"><div class="disc disc-dark">
        <svg width="26" height="26" viewBox="0 0 26 26" aria-hidden="true"><circle cx="13" cy="13" r="12" fill="#fff"/></svg>
        <span>POS &amp;<br>IT Support</span></div></div>
      <p>Lorem Ipsum is simply dummy text the printing galley of type and scrambled it to make a type</p>
      <a class="btn-more">Learn More</a>
    </div>
  </section>

  <section class="abs panel">
    <h2>Offering of General<br>IT Support</h2>
    <p>But I must explain to you how all this mistaken idea of denouncing pleasure and praising pain was born and I will give you a complete account of the system, and expound the actual teachings of the great explorer</p>
    <div class="abs panel-photo" role="img" aria-label="Photo of two businessmen meeting over coffee at a café table"></div>
    <a class="abs cta-red">LET'S MEET &nbsp;FOR COFFEE</a>
  </section>

  <section class="additional">
    <h2 class="abs tab tab-additional">Additional Services</h2>
    <div class="abs rule"></div>
    <div class="abs svc" style="top:832px;width:149px">
      <svg width="10" height="8" viewBox="0 0 10 8" aria-hidden="true"><path d="M0 7 Q2 2 7 2 V0 L10 3 L7 6 V4 Q3 4 0 7Z" fill="#fff"/></svg>Falcon Vault Storage</div>
    <div class="abs svc svc-active" style="top:856px;width:187px">
      <svg width="10" height="8" viewBox="0 0 10 8" aria-hidden="true"><path d="M0 7 Q2 2 7 2 V0 L10 3 L7 6 V4 Q3 4 0 7Z" fill="#fff"/></svg><span>Reselling and supporting<br>Corvel Shieldware</span></div>
    <div class="abs svc" style="top:896px;width:110px">
      <svg width="10" height="8" viewBox="0 0 10 8" aria-hidden="true"><path d="M0 7 Q2 2 7 2 V0 L10 3 L7 6 V4 Q3 4 0 7Z" fill="#fff"/></svg>Trelmo Suite</div>
    <p class="abs svc-copy">But I must explain to you how all this mistaken idea of denouncing pleasure and praising pain was born and I will give you a complete account of the system, and expound the actual teachings of the great explorer But I must explain to you how all this mistaken idea of denouncing pleasure and praising pain was born and I will give you a complete account of the system, and expound the actual teachings of the great explorer</p>
    <a class="abs btn-more" style="left:285px;top:901px">Learn More</a>
  </section>

  <footer>
    <div class="abs footer"></div>
    <div class="abs footer-links" style="left:68px">Home<br>About<br>Services</div>
    <div class="abs footer-links" style="left:113px">Products<br>Downloads<br>Contact</div>
    <div class="abs call-label">call us</div>
    <div class="abs phone">(0398) 4417 2260</div>
    <p class="abs footer-note">We already support hundreds of cafes and restaurants.<br>We are also about to launch and promote a range.. <a>Learn More</a></p>
    <p class="abs legal">All Right Reseved Copyright © 2012 - Privacy Policy | Terms of Use</p>
  </footer>

</div>
</body>
</html>
```